New DL Brochures for Kites Gymnastics Centres

Kites Gymnastics is about to launch its new website and to coincide with this we would like to produce a complete new set of brochures for all of our programs (10 programs)
Kites Gymnastics provides sports coaching for young children in gymnastics lessons as well as conducting holiday programs and birthday parties.
Our company colours are red, gold and black but we are trying to maintain a clean, sharp image so lots of white should be used to highlight our colours.
The brochures should all follow the same template and be clean, fresh, simple and exciting making you want to use our services.
Each brochure should contain 1 or 2 pictures (you decide !) as well as our logo (ideally at the top) with our contact details at the bottom (contact details will be required to be changed for each of our 4 locations)
We have a supply of images which will replace the stock photo supplied for the winning bid.
UPDATE - I will consider postcard type designs which may allow a more diverse range of ideas - this could be very effective way to display the information
Updates
Project Deadline Extended
Reason: I have increased the budget and would like to encourage more designs :)
I am now considering postcard type designs for this project as well as DL sized designs. After looking over a couple of designs it may be possible to do a great "postcard" style design with a great picture and basic info on the front and program info on the back of the postcard
Hi All,
Target Market(s)
Parents of young children
Industry/Entity Type
It Company
Look and feel
Each slider illustrates characteristics of the customer's brand and the style your logo design should communicate.

```html
<!DOCTYPE html>
<html lang="en">
<head>
<meta charset="utf-8">
<title>Mini Kite Postcards – Kites Gymnastics</title>
<link rel="stylesheet" href="https://fonts.googleapis.com/css2?family=Open+Sans:ital,wght@0,400;0,600;0,700;1,400&family=Alfa+Slab+One&family=Archivo+Narrow:wght@400;500&display=swap">
<style>
:root{
  --red:#d9251d;
  --red-soft:#e0514c;
  --gold:#d9b53d;
  --black:#231f20;
  --charcoal:#3a3a3a;
  --grey:#d9d9d9;
  --grey-text:#5a5a5a;
  --white:#ffffff;
  --stage:#2e2e2e;
  --label:#dcdcdc;
  --photo-a:#e8e2dc;
  --photo-b:#b58a62;
}
*{box-sizing:border-box;margin:0;padding:0}
html,body{width:1200px;height:848px;overflow:hidden;background:var(--stage)}
body{position:relative;font-family:"Open Sans",Arial,sans-serif}
.side-label{position:absolute;color:var(--label);font-size:30px;font-weight:400;letter-spacing:.5px}
.card{position:absolute;overflow:hidden;background:var(--white)}
.card svg.shapes{position:absolute;left:0;top:0}
.photo{position:absolute;background:linear-gradient(135deg,var(--photo-a) 0%,#d7c8b8 55%,var(--photo-b) 100%)}
.photo.warm{background:linear-gradient(120deg,#c9c9c9 0%,#d24a3a 45%,#c99a6a 100%)}
.abs{position:absolute}
.brand{font-size:10px;font-weight:600;color:var(--black);display:flex;align-items:center;gap:5px;line-height:1}
.brand .dot{width:9px;height:9px;border-radius:50%;background:var(--red)}
/* card 1 */
.c1{left:104px;top:110px;width:428px;height:302px}
.c1 .title{left:26px;top:36px;color:var(--white);font-size:34px;font-weight:700;letter-spacing:.5px}
.c1 .ages{left:150px;top:78px;color:var(--white);font-size:8px;font-style:italic}
.c1 .quote{left:18px;top:122px;width:180px;color:var(--white);font-size:9px;text-align:center;line-height:1.35}
.c1 .perks{left:14px;top:166px;width:190px;color:var(--white);font-size:8px;text-align:center;line-height:1.5}
.c1 .contact{left:10px;top:222px;width:160px;color:var(--black);font-size:11px;text-align:center;line-height:1.6}
.c1 .contact b{font-size:11.5px}
/* card 2 */
.c2{left:579px;top:110px;width:425px;height:302px;background:var(--charcoal)}
.c2 .quote{left:330px;top:26px;width:90px;color:var(--white);font-size:12px;text-align:center;line-height:1.3}
.c2 .title{left:38px;top:208px;font-family:"Alfa Slab One",Georgia,serif;color:var(--black);font-size:30px;letter-spacing:1px}
.c2 .ages{left:184px;top:242px;color:var(--white);font-size:8px;font-style:italic}
.c2 .perks{left:10px;top:258px;width:235px;color:var(--white);font-size:8.5px;font-weight:700;text-align:center;line-height:1.4}
.c2 .brand{left:312px;top:180px}
.c2 .contact{left:290px;top:208px;width:132px;color:var(--black);font-size:11px;text-align:right;line-height:1.55}
/* card 3 */
.c3{left:104px;top:474px;width:430px;height:304px}
.c3 .brand{left:8px;top:18px}
.c3 .perks{left:118px;top:26px;color:var(--red);font-size:8.5px}
.c3 .title-box{left:270px;top:210px;background:var(--black);color:var(--white);font-size:17px;font-weight:700;padding:1px 10px;letter-spacing:.5px}
.c3 .ages{left:384px;top:212px;background:var(--red);color:var(--white);font-size:7.5px;padding:3px 4px}
.c3 .place{left:0;top:248px;width:430px;text-align:center;font-size:8.5px;font-weight:700;color:var(--black)}
.c3 .contact{left:0;top:260px;width:430px;text-align:center;font-size:8.5px;font-weight:700;color:var(--black)}
.c3 .contact span{padding:0 5px;border-left:1px solid var(--black)}
.c3 .contact span:first-child{border-left:none}
.c3 .rule{left:28px;top:286px;width:340px;height:2px;background:var(--gold)}
/* card 4 */
.c4{left:583px;top:474px;width:424px;height:300px}
.c4 .title{left:40px;top:12px;color:var(--grey-text);font-size:50px;font-weight:600;letter-spacing:2px}
.c4 .benefits{left:30px;top:78px;list-style:none;font-family:"Archivo Narrow",Arial,sans-serif;font-size:12px;color:var(--black);line-height:1.25}
.c4 .benefits li{position:relative;padding-left:14px}
.c4 .benefits li::before{content:"★";position:absolute;left:0;top:0;color:var(--red);font-size:10px}
.c4 .cols{left:48px;top:146px;width:330px;display:flex;gap:6px;font-family:"Archivo Narrow",Arial,sans-serif;font-size:12px;color:var(--black);line-height:1.3}
.c4 .cols p{flex:1}
.c4 .rule{left:36px;top:278px;width:350px;height:3px;background:var(--red)}
</style>
</head>
<body>

<div class="side-label" style="left:287px;top:64px">front</div>
<div class="side-label" style="left:752px;top:66px">front</div>
<div class="side-label" style="left:287px;top:430px">front</div>
<div class="side-label" style="left:757px;top:424px">back</div>

<!-- Front, version 1 -->
<section class="card c1">
  <div class="photo" style="left:150px;top:0;width:278px;height:302px" role="img" aria-label="Coach crouching in front of a row of children seated on basketballs in a gym hall"></div>
  <div class="photo warm" style="left:170px;top:205px;width:130px;height:97px" role="img" aria-label="Coach helping a young girl climb a wooden gym frame"></div>
  <svg class="shapes" width="428" height="302" viewBox="0 0 428 302" aria-hidden="true">
    <polygon points="0,0 222,0 188,118 0,118" fill="var(--red)"/>
    <polygon points="0,118 188,118 160,212 0,212" fill="var(--black)"/>
    <polygon points="0,212 185,212 170,302 0,302" fill="var(--gold)"/>
    <polygon points="300,245 428,245 428,302 300,302" fill="var(--grey)"/>
  </svg>
  <div class="abs title">MINI KITE</div>
  <div class="abs ages">(2-6 years)</div>
  <div class="abs quote">"Gymnastics educates children's bodies"</div>
  <div class="abs perks">Qualified Instructors | Great Facilities<br>Safe | Fun<br>2012 WAG Club of the Year</div>
  <div class="abs contact"><b>Ashford</b><br>03 5550 0142<br>ashford@kitesgym.co<br>m.au</div>
  <div class="abs brand" style="left:315px;top:266px"><span class="dot"></span>KITES GYMNASTICS</div>
</section>

<!-- Front, version 2 -->
<section class="card c2">
  <div class="photo" style="left:0;top:0;width:330px;height:140px" role="img" aria-label="Coach crouching in front of a row of children seated on basketballs"></div>
  <svg class="shapes" width="425" height="302" viewBox="0 0 425 302" aria-hidden="true">
    <polygon points="0,140 330,140 320,130 330,0 425,0 425,302 0,302" fill="var(--charcoal)"/>
    <path d="M0,128 L0,302 L240,302 Q258,302 252,285 L238,222 Q233,204 214,201 Z" fill="var(--red)"/>
    <path d="M330,0 L425,0 L425,84 L318,84 Q304,84 308,70 Z" fill="var(--gold)"/>
    <path d="M300,104 Q286,104 283,118 L255,302 L425,302 L425,104 Z" fill="var(--grey)"/>
  </svg>
  <div class="abs quote">"Gymnastics educates children's</div>
  <div class="abs brand"><span class="dot"></span>KITES GYMNASTICS</div>
  <div class="abs contact"><b>Ashford</b><br>03 5550 0142<br>ashford@kitesgym.co<br>m.au</div>
  <div class="abs title">MINI KITE</div>
  <div class="abs ages">(2-6 years)</div>
  <div class="abs perks">Qualified Instructors | Great Facilities |Safe | Fun<br>2012 WAG Club of the Year</div>
</section>

<!-- Front, version 3 -->
<section class="card c3">
  <svg class="shapes" width="430" height="304" viewBox="0 0 430 304" aria-hidden="true">
    <rect x="0" y="40" width="430" height="166" fill="var(--grey)"/>
  </svg>
  <div class="photo warm" style="left:90px;top:40px;width:240px;height:166px" role="img" aria-label="Smiling coach helping a young girl on a wooden gym frame"></div>
  <svg class="shapes" width="430" height="304" viewBox="0 0 430 304" aria-hidden="true">
    <polygon points="0,40 66,40 0,150" fill="var(--red-soft)"/>
    <polygon points="66,40 98,40 0,203 0,150" fill="var(--black)"/>
    <polygon points="98,40 122,40 22,206 0,206 0,203" fill="#2b2b2b"/>
    <polygon points="430,42 430,206 330,206 404,42" fill="var(--gold)"/>
    <polygon points="430,120 430,206 380,206" fill="var(--red)"/>
  </svg>
  <div class="abs brand"><span class="dot"></span>KITES GYMNASTICS</div>
  <div class="abs perks">Qualified Instructors | Great Facilities |Safe | Fun &nbsp; 2012 WAG Club of the Year</div>
  <div class="abs title-box">MINI KITE</div>
  <div class="abs ages">(2-6 years)</div>
  <div class="abs place">Ashford</div>
  <div class="abs contact"><span>03 5550 0142 &nbsp;ashford@kitesgym.com.au</span><span>48 Harlow Rd, New Ashford</span><span>1300 KITE GYM (5483 496)</span></div>
  <div class="abs rule"></div>
</section>

<!-- Back -->
<section class="card c4">
  <svg class="shapes" width="424" height="300" viewBox="0 0 424 300" aria-hidden="true">
    <polygon points="0,0 88,0 0,110" fill="#f3c4c4"/>
    <polygon points="88,0 150,0 40,130 0,150 0,110" fill="#f8e0df"/>
    <polygon points="150,0 172,0 60,140 40,130" fill="#f2f2f2"/>
    <polygon points="424,210 424,290 380,290" fill="#f7eed7"/>
  </svg>
  <h1 class="abs title">MINI KITE</h1>
  <ul class="abs benefits">
    <li>Develops amazing self confidence</li>
    <li>Builds spatial awareness</li>
    <li>Builds strength, coordination and flexibility</li>
    <li>Improves the vestibular system - important for</li>
  </ul>
  <div class="abs cols">
    <p>The Mini Kites Program is designed to give children 2-6 years of age the best start in life. At Kites we use gymnastics to teach children how to move their</p>
    <p>so much more. Mini Kites incorporates all of our wonderful gymnastics apparatus such as ropes, rings, trampolines, balance</p>
    <p>gymnastics skills and concepts such as colours, numbers, shapes etc, which helps students maximise their learning opportunities.</p>
  </div>
  <div class="abs rule"></div>
</section>

</body>
</html>
```